Inspirational Quote Poster for Employees

For this project, we need a simple yet high-impact poster template that will be customized for each of our employees with a personalized inspirational quote and color scheme. This template should allow us to quickly and easily customize the text and colors in the poster without a lot of effort.

The poster design should consist of:
- A stylized text area to contain the main text of the quote
- A separate text area to contain the source of quote
- A background that complements the color and style of the text

Text may use different typographic effects (such as color, stroke weight, italicization, font size changes, drop shadows) to draw attention to words in the quote; the source of the quote may be formatted the same as the main text of the quote, or may be formatted differently to distinguish it from the main quote.

The background may be simply a single color, subtle texture, gradients, halftone effects, or other color/texture effects may be used to complement the text.

Examples of the types of posters envisioned by this project:
- http://www.tackvale.com/corwinpmaddox/artquarry-job-1/

Sample quotes to use to build your poster - choose whichever one you want, but be certain that the poster design will handle both long and short quotes:
- "Happiness in intelligent people is the rarest thing I know" - Bertram Faulconer
- "Wanting to be someone else is a waste of the person you are." - Miles Tavenor
- "Experience is not what happens to you. It is what you do with what happens to you." - Cyril Pembrage
- "Simplicity is the ultimate in sophistication." - Ottaviano Restelli
- "You will get all you want in life if you help enough other people get what they want." - Hap Dunmore
- "Hell, there are no rules here — we're trying to accomplish something." - Walter Brisbane

Quote

• Final deliverable must be:
• - Formatted for an 18” x 24” poster (in portrait orientation)
• - Delivered in Adobe InDesign, Adobe Illustrator, or Extended PostScript format
• - Use CMYK color mode
• - Be print-ready at 300dpi resolution
• - Include any fonts used in the template

```html
<!DOCTYPE html>
<html lang="en">
<head>
<meta charset="utf-8">
<title>Quote Poster</title>
<link rel="stylesheet" href="https://fonts.googleapis.com/css2?family=Oswald:wght@500&family=Roboto:ital,wght@1,700&display=swap">
<style>
  :root {
    --paper: #f4f4f4;
    --sky-light: #9cd7e6;
    --sky-mid: #7cc3d8;
    --sky-deep: #5ba6c4;
    --quote-red: #e0322f;
    --quote-mark: #ffffff;
    --band-red: #a31d1f;
    --band-text: #ffffff;
  }
  html, body {
    margin: 0;
    padding: 0;
    width: 800px;
    height: 1200px;
    overflow: hidden;
    background: var(--paper);
  }
  .poster {
    position: relative;
    width: 800px;
    height: 1200px;
    background: var(--paper);
    overflow: hidden;
  }
  .poster__field {
    position: absolute;
    left: 28px;
    top: 28px;
    width: 744px;
    height: 1144px;
    background:
      radial-gradient(ellipse 60% 55% at 50% 48%, var(--sky-light) 0%, var(--sky-mid) 60%, var(--sky-deep) 100%);
  }
  .quote {
    position: absolute;
    left: 140px;
    top: 260px;
    margin: 0;
    font-family: 'Oswald', 'Arial Narrow', sans-serif;
    font-weight: 500;
    font-size: 94px;
    line-height: 136px;
    letter-spacing: -1px;
    color: var(--quote-red);
    text-transform: uppercase;
    transform: scaleX(0.78);
    transform-origin: left top;
    white-space: nowrap;
  }
  .quote__line { display: block; }
  .quote-mark {
    position: absolute;
    font-family: 'Oswald', 'Arial Narrow', sans-serif;
    font-weight: 500;
    font-size: 120px;
    line-height: 1;
    color: var(--quote-mark);
  }
  .quote-mark--open { left: 78px; top: 258px; }
  .quote-mark--close { left: 656px; top: 678px; }
  .attribution {
    position: absolute;
    left: 288px;
    top: 928px;
    width: 484px;
    height: 40px;
  }
  .attribution__band {
    position: absolute;
    inset: 0;
    width: 100%;
    height: 100%;
  }
  .attribution__name {
    position: absolute;
    left: 40px;
    top: 0;
    line-height: 40px;
    font-family: 'Roboto', Arial, sans-serif;
    font-style: italic;
    font-weight: 700;
    font-size: 29px;
    letter-spacing: 0.5px;
    color: var(--band-text);
    text-transform: uppercase;
    white-space: nowrap;
    margin: 0;
  }
</style>
</head>
<body>
  <main class="poster">
    <div class="poster__field"></div>
    <span class="quote-mark quote-mark--open" aria-hidden="true">&ldquo;</span>
    <blockquote class="quote">
      <span class="quote__line">Wanting to be</span>
      <span class="quote__line">someone else</span>
      <span class="quote__line">is a waste of the</span>
      <span class="quote__line">person you are.</span>
    </blockquote>
    <span class="quote-mark quote-mark--close" aria-hidden="true">&rdquo;</span>
    <div class="attribution">
      <svg class="attribution__band" viewBox="0 0 484 40" preserveAspectRatio="none" aria-hidden="true">
        <polygon points="10,0 484,0 484,40 0,40" fill="var(--band-red)"/>
      </svg>
      <p class="attribution__name">- Miles Tavenor</p>
    </div>
  </main>
</body>
</html>
```